Email Marketing Campaign 50% discount and buy-2-get-1 offer

I would like to inform my customers of our special offers via a e-Newsletter/Marketing E-Mail.

The coding needs to be done by the designer.

I have most of the design and the message that we wish to convey our buyers.

The information is:

1. We have now 50% discount on all our carpets

2. We have a buy-2 get-1 free carpet offer

For both the above messages we have already banner style that we like to use in our Newsletter.
I have attached the banner and the designers can use it.

3. We have opened a new shop in Berlin Germany

Therefore we like to have a Sylish Newsletter design that fits our website and products using the banner idea and we wish to include the 3 messages.
Special note should be given that this newsletter is going to our previous buyers. Therefore they already know us, and we just like to inform them of our latest news and offer.

Target Market(s)

Upmarket buyers looking for a great deal

Industry/Entity Type

Marketing

Coding

Coded - Design and coding required

Number of Pages Required

1 page

Font styles to use
Sans Serif

Colors
e667a6
34a7d8

Requirements
Must have
• Clear explanation with excitement in the message
Nice to have
• To promote clearly the 3 for 2 with maybe an explanation and clear images describing what the promotion is and how it works.
• I.e. buy 2 get 1 extra carpet of your choice free
• Add carpets to checkout and the system will calculate automatically
• The lowest carpet in your selection of 3 is the free carpet

```html
<!DOCTYPE html>
<html lang="en">
<head>
<meta charset="utf-8">
<title>Loomhaven – Biggest Carpet Sale of the Year</title>
<link href="https://fonts.googleapis.com/css2?family=Dancing+Script:wght@600;700&family=Open+Sans:wght@400;600;700&display=swap" rel="stylesheet">
<style>
  :root {
    --frame: #16a7b8;
    --notice: #ffb300;
    --paper: #ffffff;
    --pink: #ec1a8c;
    --blue: #1e8ad8;
    --ink: #1b1b1b;
    --grey: #6f6f6f;
    --ribbon: #5ec81d;
    --ribbon-dark: #3e8a10;
    --coupon-bg: #f4f5f7;
    --cyan: #00e4ec;
    --orange: #f7a646;
    --lime: #9cf02c;
    --gold: #ffdf3a;
    --social-bar: #2a2a2a;
  }
  * { box-sizing: border-box; margin: 0; padding: 0; }
  html, body { width: 1200px; height: 3063px; overflow: hidden; }
  body {
    background: var(--frame);
    font-family: "Open Sans", Arial, sans-serif;
    color: var(--ink);
    position: relative;
  }
  .notice-bar {
    position: absolute; left: 45px; top: 30px; width: 1110px; height: 83px;
    background: var(--notice);
    display: flex; align-items: center; justify-content: center;
    font-size: 25px; color: var(--ink);
  }
  .notice-bar a { color: #fff; text-decoration: none; }
  .sheet {
    position: absolute; left: 45px; top: 143px; width: 1110px; height: 2845px;
    background: var(--paper);
  }
  .brand {
    position: absolute; left: 0; width: 1110px; top: 50px; text-align: center;
    font-size: 88px; font-weight: 400; letter-spacing: 6px; color: var(--grey);
    line-height: 1;
  }
  .headline {
    position: absolute; left: 0; width: 1110px; top: 210px; text-align: center;
    font-family: "Dancing Script", cursive; font-weight: 700;
    font-size: 118px; color: var(--pink); line-height: 1.1;
  }
  .subhead {
    position: absolute; left: 0; width: 1110px; top: 370px;
    display: flex; align-items: center; justify-content: center; gap: 22px;
    font-size: 42px; font-weight: 700; color: var(--blue); letter-spacing: 2px;
  }
  .subhead::before, .subhead::after {
    content: ""; width: 170px; height: 3px; background: var(--blue);
  }
  .hero {
    position: absolute; left: 39px; top: 445px; width: 1038px; height: 612px;
    background: linear-gradient(180deg, #d9d3cc 0%, #c9c0b8 45%, #8a6f66 62%, #b58783 78%, #4c3a33 100%);
  }
  .hero-burst { position: absolute; left: 21px; top: 172px; width: 270px; height: 270px; }
  .hero-offer {
    position: absolute; left: 306px; top: 215px; width: 732px; height: 170px;
    background: linear-gradient(90deg, rgba(25,25,25,0.2) 0%, rgba(25,25,25,0.75) 12%, rgba(25,25,25,0.75) 100%);
    display: flex; flex-direction: column; justify-content: center; padding-left: 60px; gap: 12px;
    white-space: nowrap;
  }
  .hero-offer .line-one { font-size: 34px; color: #fff; }
  .hero-offer .line-one strong { color: var(--lime); font-weight: 700; }
  .hero-offer .line-two { font-size: 36px; color: var(--gold); }
  .ribbon { position: absolute; left: -15px; top: 1081px; width: 1140px; height: 150px; }
  .ribbon-text {
    position: absolute; left: 0; width: 1110px; top: 1081px; height: 120px;
    display: flex; align-items: center; justify-content: center;
    font-size: 64px; color: #fff; font-weight: 400;
  }
  .ribbon-text small { font-size: 44px; margin: 0 14px; }
  .coupon {
    position: absolute; left: 39px; top: 1207px; width: 1038px; height: 525px;
    background: var(--coupon-bg);
  }
  .coupon-bracket { position: absolute; left: 80px; top: 42px; width: 433px; height: 100px; }
  .tag-buy {
    position: absolute; left: 185px; top: 42px; width: 316px; height: 78px;
    background: #fff; border: 3px solid var(--orange);
    display: flex; align-items: center; justify-content: center;
    font-size: 46px; font-weight: 700; color: #333;
  }
  .tag-free {
    position: absolute; left: 737px; top: 42px; width: 240px; height: 78px;
    background: var(--pink);
    display: flex; align-items: center; justify-content: center;
    font-size: 46px; font-weight: 700; color: #fff;
  }
  .rug {
    position: absolute; top: 165px; width: 300px; height: 300px; border-radius: 50%;
    border: 12px solid #fff; box-shadow: 0 4px 14px rgba(0,0,0,0.25);
  }
  .rug-one { left: 15px; background: radial-gradient(circle, #6b5b62 0%, #3a2f35 60%, #1f1a1e 100%); }
  .rug-two { left: 358px; background: radial-gradient(circle, #d76c5c 0%, #c0655a 50%, #9a8270 100%); }
  .rug-three { left: 722px; background: radial-gradient(circle, #e7a29c 0%, #dd9a92 55%, #c98c88 100%); }
  .berlin {
    position: absolute; left: 39px; top: 1786px; width: 1038px; height: 486px;
    background: var(--cyan); color: #fff; text-align: center;
  }
  .berlin-title {
    position: absolute; left: 0; width: 100%; top: 28px;
    font-family: "Dancing Script", cursive; font-weight: 700; font-size: 84px; line-height: 1.1;
  }
  .berlin-address {
    position: absolute; left: 0; width: 100%; top: 146px;
    font-size: 40px; line-height: 50px; letter-spacing: 1px;
  }
  .berlin-button {
    position: absolute; left: 246px; top: 285px; width: 540px; height: 120px;
    background: #000; border: 4px solid #fff;
    display: flex; align-items: center; justify-content: center;
    font-size: 44px; color: #fff; text-decoration: none;
  }
  .details {
    position: absolute; top: 2340px; font-size: 32px; line-height: 44px; white-space: nowrap;
  }
  .details h2 { font-size: 34px; font-weight: 700; margin-bottom: 14px; }
  .details-address { left: 39px; }
  .details-contact { left: 680px; }
  .details-contact b { font-weight: 700; }
  .social {
    position: absolute; left: 39px; top: 2562px; width: 1038px; height: 150px;
    background: var(--social-bar); border-radius: 14px;
    display: flex; align-items: center; justify-content: center; gap: 30px;
  }
  .social-chip { width: 96px; height: 96px; border-radius: 18px; }
  .chip-video { background: #b3141c; }
  .chip-pins { background: #c8232c; border-radius: 50%; }
  .chip-social { background: #3b5998; }
  .chip-mail { background: #f39c12; border-radius: 50%; display: flex; align-items: center; justify-content: center; }
  .chip-call { background: #00aff0; border-radius: 50%; }
  .copyright {
    position: absolute; left: 0; width: 1110px; top: 2750px; text-align: center;
    font-size: 26px; color: #333;
  }
</style>
</head>
<body>
  <div class="notice-bar">Having trouble seeing this mail?&nbsp;<a href="#">Click here</a>&nbsp;| Don't want to receive this?&nbsp;<a href="#">Unsubscribe</a></div>

  <main class="sheet">
    <div class="brand">LOOMHAVEN</div>
    <h1 class="headline">Biggest Carpet Sale</h1>
    <div class="subhead">OF THE YEAR</div>

    <section class="hero" role="img" aria-label="Bright living room with a sofa and a large patterned rug on a dark wooden floor">
      <div class="hero-offer">
        <div class="line-one">Buy One Carpet &amp; Get <strong>EXTRA 50% OFF</strong></div>
        <div class="line-two">OFFER VALID FOR ALL CARPETS</div>
      </div>
      <svg class="hero-burst" viewBox="0 0 270 270" aria-hidden="true">
        <polygon fill="#fff" points="135,0 152,28 180,8 188,40 220,30 218,63 251,64 238,94 268,108 246,132 268,156 238,172 251,204 218,206 220,238 188,230 180,262 152,242 135,270 118,242 90,262 82,230 50,238 52,206 19,204 32,172 2,156 24,132 2,108 32,94 19,64 52,63 50,30 82,40 90,8 118,28"/>
        <circle cx="135" cy="135" r="100" fill="var(--orange)"/>
        <text x="122" y="150" text-anchor="middle" font-family="Open Sans, sans-serif" font-weight="700" font-size="88" fill="#fff">50</text>
        <text x="190" y="118" text-anchor="middle" font-family="Open Sans, sans-serif" font-weight="700" font-size="26" fill="#fff">%</text>
        <text x="135" y="200" text-anchor="middle" font-family="Open Sans, sans-serif" font-weight="700" font-size="36" fill="#fff">OFF</text>
      </svg>
    </section>

    <svg class="ribbon" viewBox="0 0 1140 150" aria-hidden="true">
      <polygon points="0,120 30,120 30,150" fill="var(--ribbon-dark)"/>
      <polygon points="1140,120 1110,120 1110,150" fill="var(--ribbon-dark)"/>
      <rect x="0" y="0" width="1140" height="120" fill="var(--ribbon)"/>
    </svg>
    <div class="ribbon-text">3<small>FOR</small>2 COUPON</div>

    <section class="coupon">
      <svg class="coupon-bracket" viewBox="0 0 433 100" aria-hidden="true">
        <polyline points="2,100 2,40 431,40 431,100" fill="none" stroke="var(--orange)" stroke-width="3"/>
      </svg>
      <div class="tag-buy">BUY 2</div>
      <div class="tag-free">1 FREE</div>
      <div class="rug rug-one" role="img" aria-label="Dark distressed vintage rug"></div>
      <div class="rug rug-two" role="img" aria-label="Colourful patterned vintage rug"></div>
      <div class="rug rug-three" role="img" aria-label="Faded pink vintage rug"></div>
    </section>

    <section class="berlin">
      <h2 class="berlin-title">New Store in Berlin</h2>
      <div class="berlin-address">LINDENWEG 12<br>10115 BERLIN</div>
      <a class="berlin-button" href="#">Visit Us in Berlin</a>
    </section>

    <div class="details details-address">
      <h2>ADDRESS</h2>
      <p>Lindenweg 12<br>10115 Berlin</p>
    </div>
    <div class="details details-contact">
      <h2>CONTACT</h2>
      <p><b>Ph:</b> +49 30 00 41 27 90<br><b>Email:</b> hi@loomhaven.de</p>
    </div>

    <nav class="social" aria-label="Social links">
      <span class="social-chip chip-video"></span>
      <span class="social-chip chip-pins"></span>
      <span class="social-chip chip-social"></span>
      <span class="social-chip chip-mail">
        <svg width="56" height="40" viewBox="0 0 56 40" aria-hidden="true">
          <rect x="2" y="2" width="52" height="36" rx="3" fill="none" stroke="#fff" stroke-width="4"/>
          <polyline points="4,4 28,24 52,4" fill="none" stroke="#fff" stroke-width="4"/>
        </svg>
      </span>
      <span class="social-chip chip-call"></span>
    </nav>

    <div class="copyright">© 2016, ALL RIGHTS RESERVED</div>
  </main>
</body>
</html>
```